Webshop Template

For our Webstore in UK we need a complete Template,
shoppingcart is Magento, the Shop is focussed on Download software,

the name: Appvaultdepot.co.uk

Check out some other good stores, like lumawerk.de

for example the Page from 

www.brenvik.co.uk or

www.lumawerk.de

www.tastenhugo.de

www.klickrabatt.de

The Logodesign which are in Consideration

http://www.artmosaiq.com/design/5520817/logo-design-by-tomasz7kv

http://www.artmosaiq.com/design/5518360/logo-design-by-luisgaviota

http://www.artmosaiq.com/design/5517245/logo-design-by-kestrel-works

http://www.artmosaiq.com/design/5516093/logo-design-by-zumbiloft

http://www.artmosaiq.com/design/5515471/logo-design-by-tivaro

http://www.artmosaiq.com/design/5514902/logo-design-by-blue-fern-graphics-

Target Market(s)

B2C - Consumer Marcet

Industry/Entity Type

Shop

```html
<!DOCTYPE html>
<html lang="en">
<head>
<meta charset="utf-8">
<title>Appvaultdepot.co.uk – Webshop</title>
<link href="https://fonts.googleapis.com/css2?family=Ubuntu:wght@400;500;700&family=Arimo:wght@400;700&display=swap" rel="stylesheet">
<style>
:root{
  --header-bg:#1f1f1f;
  --footer-bg:#474747;
  --footer-base:#3a3a3a;
  --accent:#f26522;
  --accent-line:#e8774a;
  --blue:#1c7fd0;
  --green:#8fcf12;
  --grey-text:#5a5a5a;
  --nav-active:#2c3e5e;
  --nav-item:#d8d8d8;
  --card-border:#dedede;
  --caption-bg:#efefef;
  --ink:#222;
}
*{margin:0;padding:0;box-sizing:border-box}
html,body{width:1022px;height:1200px;overflow:hidden;background:#fff}
body{font-family:"Arimo",Arial,sans-serif;color:var(--ink)}
.page{position:relative;width:1022px;height:1200px;overflow:hidden}

/* header */
.site-header{position:absolute;left:0;top:0;width:1022px;height:112px;background:var(--header-bg)}
.brand{position:absolute;left:90px;top:30px;display:flex;align-items:center;gap:8px}
.brand-dot{width:40px;height:40px;border-radius:50%;background:var(--blue)}
.brand-name{font-family:"Ubuntu",sans-serif;font-weight:500;font-size:27px;color:#fff;letter-spacing:-.5px}
.account-links{position:absolute;right:90px;top:11px;font-size:11px;color:#ddd;word-spacing:2px}
.account-links span{margin:0 8px;color:#aaa}
.main-nav{position:absolute;right:86px;top:88px;font-family:"Ubuntu",sans-serif;font-size:12px;color:#fff}
.main-nav span{margin:0 9px;color:#ccc}

/* hero */
.hero{position:absolute;left:0;top:112px;width:1022px;height:375px;background:linear-gradient(#f2f2f2,#ececec)}
.hero-fee{position:absolute;left:121px;top:52px;font-family:"Ubuntu",sans-serif;font-weight:500;font-size:14.5px;color:var(--accent)}
.hero-fee b{font-size:21px;font-weight:700}
.hero-title{position:absolute;left:121px;top:86px;font-family:"Ubuntu",sans-serif;font-weight:700;line-height:1}
.hero-title .l1{display:block;font-size:24.5px;color:var(--blue);letter-spacing:.5px}
.hero-title .l2{display:block;font-size:32px;margin-top:9px;letter-spacing:.5px}
.hero-title .green{color:var(--green)}
.hero-title .grey{color:var(--grey-text)}
.hero-rule{position:absolute;left:123px;top:173px;width:370px;border-top:1px dotted #bbb}
.hero-copy{position:absolute;left:126px;top:194px;width:386px;font-size:10.5px;line-height:19px;color:#444;text-align:justify;letter-spacing:.3px}
.hero-copy b{color:#222}
.buy-now{position:absolute;left:129px;top:304px;width:147px;height:36px;border-radius:18px;background:linear-gradient(#6b6b6b,#3c3c3c);border:2px solid #2b2b2b;display:flex;align-items:center;padding-left:15px;font-family:"Ubuntu",sans-serif;font-size:20px;color:#fff}
.buy-now svg{position:absolute;right:8px;top:4px}
.hero-art{position:absolute;left:595px;top:16px;width:340px;height:345px;border-radius:28px;background:linear-gradient(135deg,#2a6fbf 0%,#d73c4e 45%,#1d3f7a 100%)}

/* partners */
.partners{position:absolute;left:0;top:487px;width:1022px;height:77px;background:linear-gradient(#fafafa,#e9e9e9);border-top:1px solid #e2e2e2;display:flex;justify-content:center;align-items:center;gap:26px}
.partner{font-family:"Ubuntu",sans-serif;font-weight:700;font-size:17px;color:#a9a9a9}

/* categories */
.categories{position:absolute;left:90px;top:596px;width:224px;height:387px;border:1px solid var(--card-border);padding:21px 2px 0 2px}
.categories li{list-style:none;height:23px;margin-bottom:4.2px;background:var(--nav-item);font-size:10.5px;color:#222;line-height:23px;padding-left:7px;position:relative}
.categories li::after{content:"»";position:absolute;right:7px;top:-1px;font-size:13px}
.categories li.active{background:var(--nav-active);color:#fff}

/* products */
.product{position:absolute;width:189px;height:184px;border:2px solid var(--card-border);background:#fff}
.product-shot{position:absolute;left:30px;top:8px;width:125px;height:130px;border-radius:4px}
.product-caption{position:absolute;left:4px;right:4px;bottom:4px;height:36px;background:var(--caption-bg);text-align:center;padding-top:3px}
.product-name{font-size:11px;font-weight:700;color:#444;letter-spacing:.3px}
.product-price{font-family:"Ubuntu",sans-serif;font-size:14px;font-weight:500;color:var(--accent);margin-top:2px;letter-spacing:.5px}

/* footer */
.footer{position:absolute;left:0;top:1017px;width:1022px;height:151px;background:var(--footer-bg);border-top:5px solid var(--accent-line)}
.footer-col{position:absolute;top:14px}
.footer-col h3{font-family:"Ubuntu",sans-serif;font-weight:400;font-size:17px;color:#fff;margin-bottom:6px;letter-spacing:.3px}
.footer-col li{list-style:none;font-size:10px;color:#e8e8e8;line-height:17px;letter-spacing:.6px}
.footer-col li::before{content:"»";color:var(--accent);margin-right:5px}
.footer-divider{position:absolute;top:16px;width:1px;height:120px;background:#5a5a5a}
.copyright{position:absolute;left:0;top:1168px;width:1022px;height:32px;background:var(--footer-base);color:#eee;font-size:10px;text-align:center;line-height:32px;letter-spacing:.4px}
</style>
</head>
<body>
<div class="page">

<header class="site-header">
  <div class="brand"><span class="brand-dot"></span><span class="brand-name">appvaultdepot</span></div>
  <div class="account-links">Create New Account<span>|</span>Log In<span>|</span>Contact Us<span>|</span>View Cart (0)</div>
  <nav class="main-nav">Software<span>|</span>Computer &amp; Hardware<span>|</span>Printer<span>|</span>Displays<span>|</span>Notebooks<span>|</span>Telecommunications</nav>
</header>

<section class="hero">
  <p class="hero-fee">The service/product will be paid for by a monthly <b>($5)</b> fee.</p>
  <h1 class="hero-title"><span class="l1">BEST SOFTWARE PRODUCTS FOR</span><span class="l2"><span class="green">APPVAULT</span> <span class="grey">DEPOT</span></span></h1>
  <div class="hero-rule"></div>
  <p class="hero-copy"><b>Lorem ipsum dolor sit amet conse ctetur adipisicing elit, sed do eiusmod tempor incididunt ut labore et dolore</b> magna aliqua.Ut enim ad minim veniam, quis nostrud exercitation ullamco laboris nisi ut aliquip.Ut enim ad minim veniam, quis nostrud exercitation ullamco laboris nisi ut aliquip.</p>
  <div class="buy-now">Buy Now
    <svg width="24" height="24" viewBox="0 0 24 24"><circle cx="12" cy="12" r="11" fill="#f4f4f4" stroke="#999"/><path d="M10 7.5 15 12 10 16.5Z" fill="#444"/></svg>
  </div>
  <div class="hero-art" role="img" aria-label="Smartphone surrounded by colourful sale tickets, discount tags and a payment card"></div>
</section>

<section class="partners">
  <span class="partner">Tollway Pay</span>
  <span class="partner">Kardio</span>
  <span class="partner">Searchly</span>
  <span class="partner">Paymint</span>
  <span class="partner">Trustmark</span>
  <span class="partner">Friendloop</span>
  <span class="partner">Workweave</span>
  <span class="partner">Chirpline</span>
</section>

<ul class="categories">
  <li class="active">Software</li>
  <li>Zeno Games</li>
  <li>Vortabox Games</li>
  <li>PC Software</li>
  <li>Word Software</li>
  <li>Antivirus</li>
  <li>Panelux Software</li>
  <li>Accounts Software</li>
  <li>Vantra Software</li>
  <li>KV Software</li>
  <li>Pearfield Software</li>
  <li>Tapfone Games</li>
  <li>Mobile Phone Games</li>
</ul>

<article class="product" style="left:337px;top:596px">
  <div class="product-shot" role="img" aria-label="Dark software box with orange emblem" style="background:linear-gradient(#3a4048,#1e2228)"></div>
  <div class="product-caption"><div class="product-name">Promotional Picnic Sets</div><div class="product-price">$ 125.000</div></div>
</article>
<article class="product" style="left:541px;top:596px">
  <div class="product-shot" role="img" aria-label="Orange software pack box with blue shield" style="background:linear-gradient(135deg,#f7a21b,#e2452a)"></div>
  <div class="product-caption"><div class="product-name">Promotional Picnic Sets</div><div class="product-price">$ 125.000</div></div>
</article>
<article class="product" style="left:745px;top:596px">
  <div class="product-shot" role="img" aria-label="Blue internet security software box" style="background:linear-gradient(#2d74c4,#e9eef5)"></div>
  <div class="product-caption"><div class="product-name">Promotional Picnic Sets</div><div class="product-price">$ 125.000</div></div>
</article>
<article class="product" style="left:337px;top:800px">
  <div class="product-shot" role="img" aria-label="Purple PC repair software case with disc" style="background:linear-gradient(135deg,#3a2360,#8a8a9a)"></div>
  <div class="product-caption"><div class="product-name">Promotional Picnic Sets</div><div class="product-price">$ 125.000</div></div>
</article>
<article class="product" style="left:541px;top:800px">
  <div class="product-shot" role="img" aria-label="Karaoke software disc" style="border-radius:50%;left:35px;width:118px;height:118px;top:12px;background:radial-gradient(#d99a6a,#5a2a1a)"></div>
  <div class="product-caption"><div class="product-name">Promotional Picnic Sets</div><div class="product-price">$ 125.000</div></div>
</article>
<article class="product" style="left:745px;top:800px">
  <div class="product-shot" role="img" aria-label="Accounting software box with disc" style="background:linear-gradient(#ffffff 0%,#ffffff 35%,#4a78b8 60%,#9cc26a 100%)"></div>
  <div class="product-caption"><div class="product-name">Promotional Picnic Sets</div><div class="product-price">$ 125.000</div></div>
</article>

<footer class="footer">
  <div class="footer-col" style="left:133px"><h3>Sound</h3><ul><li>Powered Speakers Budget</li><li>Power Amplifiers</li><li>Active Speakers</li><li>Passive Speakers</li><li>Split Systems</li></ul></div>
  <div class="footer-divider" style="left:284px"></div>
  <div class="footer-col" style="left:306px"><h3>Accessories</h3><ul><li>Hardware</li><li>DJ Gear Spare Parts</li><li>Drivers / Tweeters / X-Overs</li><li>Power Supplies</li><li>Electronics</li></ul></div>
  <div class="footer-divider" style="left:471px"></div>
  <div class="footer-col" style="left:494px"><h3>Packages</h3><ul><li>Home Audio</li><li>DJ Packages</li><li>Speaker Packs</li><li>Lighting Packs</li><li>PA Packages</li></ul></div>
  <div class="footer-divider" style="left:612px"></div>
  <div class="footer-col" style="left:643px"><h3>Stands Brackets</h3><ul><li>Clamps</li><li>Lighting Stands</li><li>DJ Stands</li><li>Speaker Stands</li><li>Music Stands</li></ul></div>
  <div class="footer-divider" style="left:788px"></div>
  <div class="footer-col" style="left:817px"><h3>Brands</h3><ul><li>Home Audio</li><li>DJ Packages</li><li>Speaker Packs</li><li>Lighting Packs</li><li>PA Packages</li></ul></div>
</footer>
<div class="copyright">Copyright 2008 Appvaultdepot.co.uk.</div>

</div>
</body>
</html>
```